Deactivated Coal-Fired Power Plant to be redeveloped into a Green Energy Campus.

Want a striking business card statement that introduces our concept project to provide economic and community recovery to a former rural coal community in western PA.
Essentially 12 project representatives that will lead both the demolition of an existing power plant and the redevelopment to a new Green energy site.
Business Card should reflect our effort.
We are open to ideas.

Target Market(s)

Energy and Power Generation industries

Industry/Entity Type

Power Generation and Data Centers

Contact Information for Business Card

Included in uploaded materials

Font styles to use
Sans Serif
Other font styles liked:
• Arial, Calibri

Requirements
Must have
• Multiple colors

```html
<!DOCTYPE html>
<html lang="en">
<head>
<meta charset="utf-8">
<title>Ridgeline Renewal – Business Card</title>
<link href="https://fonts.googleapis.com/css2?family=Montserrat:wght@400;500;700;800&display=swap" rel="stylesheet">
<style>
  :root {
    --page: #3a3a3a;
    --green: #139a48;
    --ink: #111111;
    --card-dark: #161616;
    --card-light: #ffffff;
    --soft-white: #f2f2f2;
    --rule: #5a5a5a;
  }
  * { box-sizing: border-box; margin: 0; padding: 0; }
  html, body {
    width: 1200px; height: 1200px; overflow: hidden;
    background: var(--page);
    font-family: "Montserrat", Arial, sans-serif;
  }
  .sheet {
    width: 1200px; height: 1200px;
    display: flex; flex-direction: column; align-items: center; justify-content: center;
    gap: 60px;
  }
  .card {
    position: relative;
    width: 840px; height: 480px;
    border-radius: 36px;
    overflow: hidden;
    border-bottom: 4px solid var(--green);
  }
  .card--statement { background: var(--card-light); color: var(--ink); }
  .card--contact { background: var(--card-dark); color: var(--soft-white); }

  .brand {
    display: flex; align-items: center; justify-content: center; gap: 16px;
    font-weight: 800; text-transform: uppercase; letter-spacing: 1px;
  }
  .brand__dot { border-radius: 50%; background: var(--green); flex: none; }

  .card--statement .brand { margin-top: 92px; font-size: 34px; color: var(--ink); }
  .card--statement .brand__dot { width: 40px; height: 40px; }
  .statement__heading {
    margin-top: 64px; text-align: center;
    color: var(--green); font-weight: 500; font-size: 30px; letter-spacing: 1px;
  }
  .statement__body {
    width: 600px; margin: 14px auto 0;
    text-align: center; font-weight: 800; font-size: 17px; line-height: 1.5;
  }

  .card--contact .brand { margin-top: 110px; font-size: 42px; color: #ffffff; }
  .card--contact .brand__dot { width: 50px; height: 50px; }
  .holder {
    position: absolute; left: 64px; bottom: 60px;
  }
  .holder__name { color: var(--green); font-weight: 500; font-size: 38px; line-height: 1; }
  .holder__title { color: #ffffff; font-size: 17px; margin-top: 6px; }
  .divider {
    position: absolute; left: 470px; bottom: 56px;
    width: 1px; height: 90px; background: var(--rule);
  }
  .contacts {
    position: absolute; left: 510px; bottom: 62px;
    list-style: none; font-size: 19px; font-weight: 400;
  }
  .contacts li { display: flex; align-items: center; gap: 12px; height: 30px; }
  .contacts svg { width: 20px; height: 20px; flex: none; }
</style>
</head>
<body>
<main class="sheet">

  <section class="card card--statement">
    <div class="brand"><span class="brand__dot"></span><span>Ridgeline Renewal</span></div>
    <h2 class="statement__heading">STATEMENT</h2>
    <p class="statement__body">Lorem ipsum dolor sit amet conse tetuer adipiscing elit, sed diam nonummy nibh euismod tincidunt ut laoreet dolore magna aliquam erat sed diam nonummy nibh euismod tincidunt ut laoreet dolore magna aliquam erat</p>
  </section>

  <section class="card card--contact">
    <div class="brand"><span class="brand__dot"></span><span>Ridgeline Renewal</span></div>

    <div class="holder">
      <p class="holder__name">FULL NAME</p>
      <p class="holder__title">TITLE</p>
    </div>

    <span class="divider"></span>

    <ul class="contacts">
      <li>
        <svg viewBox="0 0 24 24" aria-hidden="true"><path fill="#139a48" d="M6.6 10.8a15.1 15.1 0 0 0 6.6 6.6l2.2-2.2c.3-.3.7-.4 1-.2 1.1.4 2.3.6 3.6.6.6 0 1 .4 1 1V20c0 .6-.4 1-1 1A17 17 0 0 1 3 4c0-.6.4-1 1-1h3.5c.6 0 1 .4 1 1 0 1.3.2 2.5.6 3.6.1.3 0 .7-.2 1z"/></svg>
        <span>(000) 000 0000</span>
      </li>
      <li>
        <svg viewBox="0 0 24 24" aria-hidden="true"><rect x="6" y="2" width="12" height="20" rx="2" fill="none" stroke="#139a48" stroke-width="2"/><circle cx="12" cy="18" r="1.2" fill="#139a48"/></svg>
        <span>(000) 000 0000</span>
      </li>
      <li>
        <svg viewBox="0 0 24 24" aria-hidden="true"><rect x="2" y="5" width="20" height="14" fill="#139a48"/><path d="M2 5l10 8 10-8" fill="none" stroke="#161616" stroke-width="1.6"/></svg>
        <span>email@company.com</span>
      </li>
    </ul>
  </section>

</main>
</body>
</html>
```